Bref créative
business stationary package for dex9firm
envelopes, business cards, 2xcover sheets,ppt template, letterhead, mousepad, cd
Professional
Tobias Wendt
Lindmoosweg 7c
A-4820 Bad Ischl
tobias.wendt@dex9firm-example.at
www.dex9firm-example.at
We would need the following templates:
1) letterhead in the size A4
2) ppt presentation in the size A4 landscape
3) business cards in the size of 3.47x2.25in (88,22x57,22mm)
4) single page cover sheet for encrypted emails (A4 portrait)
5) cover sheet for handouts (A4 portrait)
6) mouse pad
7) cd cover sheet+cd design
8) envelope
dex9firm logo
mind: usage without the mirroring effect
demo encrypted message coversheet - ours should look similar but in the dex9firm design - having the same content - we should be able to edit the text
demo for other coversheet - a free rectangle area (cut out) should be placed similar to this upload. We want to print the title on the following page and it should be visible through this cover sheet.

```html
<!DOCTYPE html>
<html lang="en">
<head>
<meta charset="utf-8">
<title>dex9firm business cards</title>
<link href="https://fonts.googleapis.com/css2?family=Exo+2:wght@700&family=Open+Sans:wght@400;600&display=swap" rel="stylesheet">
<style>
  :root {
    --page-bg: #e9ecef;
    --blue-deep: #0f4f8c;
    --blue-mid: #1f6fb5;
    --blue-light: #3d8fd3;
    --white: #ffffff;
    --swoosh-grey: #b9bec4;
    --logo-blue: #1a5a9c;
  }
  html, body {
    margin: 0;
    width: 1200px;
    height: 991px;
    overflow: hidden;
    background: var(--page-bg);
  }
  .stage {
    position: relative;
    width: 1200px;
    height: 991px;
    display: flex;
    align-items: center;
    justify-content: center;
    gap: 40px;
  }
  .card {
    position: relative;
    width: 540px;
    height: 350px;
    border-radius: 22px;
    overflow: hidden;
    box-shadow: 0 10px 28px rgba(0, 0, 0, 0.18);
  }
  .card-art {
    position: absolute;
    inset: 0;
  }
  .wordmark {
    position: absolute;
    font-family: "Exo 2", sans-serif;
    font-weight: 700;
    letter-spacing: -1px;
    line-height: 1;
    white-space: nowrap;
  }
  .card--back {
    background: radial-gradient(ellipse at 50% 40%, var(--blue-light) 0%, var(--blue-mid) 45%, var(--blue-deep) 100%);
  }
  .card--back .wordmark {
    left: 0;
    right: 0;
    top: 112px;
    text-align: center;
    font-size: 66px;
    color: var(--white);
  }
  .web-address {
    position: absolute;
    left: 0;
    right: 0;
    top: 205px;
    text-align: center;
    font-family: "Open Sans", sans-serif;
    font-size: 13px;
    letter-spacing: 5px;
    color: var(--white);
  }
  .card--front {
    background: var(--blue-mid);
  }
  .card--front .wordmark {
    left: 270px;
    top: 82px;
    font-size: 58px;
    color: var(--logo-blue);
  }
  .contact-list {
    position: absolute;
    left: 22px;
    top: 168px;
    margin: 0;
    padding: 0;
    list-style: none;
    font-family: "Open Sans", sans-serif;
    font-size: 11px;
    color: var(--white);
  }
  .contact-list li {
    display: flex;
    align-items: center;
    gap: 8px;
    height: 19px;
  }
  .contact-icon {
    width: 11px;
    height: 11px;
    flex: none;
  }
  .holder-name {
    position: absolute;
    right: 26px;
    bottom: 22px;
    font-family: "Open Sans", sans-serif;
    font-weight: 600;
    font-size: 16px;
    color: var(--white);
  }
</style>
</head>
<body>
<main class="stage">

  <section class="card card--front" aria-label="Business card front">
    <svg class="card-art" viewBox="0 0 540 350" aria-hidden="true">
      <defs>
        <linearGradient id="front-blue" x1="0" y1="0" x2="1" y2="1">
          <stop offset="0" stop-color="#3d8fd3"/>
          <stop offset="0.6" stop-color="#1f6fb5"/>
          <stop offset="1" stop-color="#0f4f8c"/>
        </linearGradient>
        <linearGradient id="front-white" x1="0" y1="0" x2="0" y2="1">
          <stop offset="0" stop-color="#ffffff"/>
          <stop offset="1" stop-color="#eceef0"/>
        </linearGradient>
      </defs>
      <rect width="540" height="350" fill="url(#front-blue)"/>
      <path d="M150,0 C205,175 370,232 540,226 L540,0 Z" fill="#b9bec4"/>
      <path d="M170,0 C225,165 380,215 540,208 L540,0 Z" fill="url(#front-white)"/>
    </svg>

    <div class="wordmark">dex9firm</div>

    <ul class="contact-list">
      <li><svg class="contact-icon" viewBox="0 0 12 12"><circle cx="6" cy="6" r="6" fill="#fff"/><path d="M6 2.5a2 2 0 0 0-2 2c0 1.6 2 4.5 2 4.5s2-2.9 2-4.5a2 2 0 0 0-2-2z" fill="#1f6fb5"/></svg>Lindmoosweg 7c, A-4820 Bad Ischl</li>
      <li><svg class="contact-icon" viewBox="0 0 12 12"><circle cx="6" cy="6" r="6" fill="#fff"/><rect x="4" y="3" width="4" height="6" rx="1" fill="#1f6fb5"/></svg>+43 1 5550172 0</li>
      <li><svg class="contact-icon" viewBox="0 0 12 12"><circle cx="6" cy="6" r="6" fill="#fff"/><rect x="4.3" y="2.5" width="3.4" height="7" rx="0.8" fill="#1f6fb5"/></svg>+43 664 5550172 48</li>
      <li><svg class="contact-icon" viewBox="0 0 12 12"><circle cx="6" cy="6" r="6" fill="#fff"/><rect x="3" y="4" width="6" height="4" fill="#1f6fb5"/></svg>+43 1 5550172 99</li>
      <li><svg class="contact-icon" viewBox="0 0 12 12"><circle cx="6" cy="6" r="6" fill="#fff"/><rect x="3" y="4" width="6" height="4" fill="none" stroke="#1f6fb5"/><path d="M3 4l3 2.2L9 4" fill="none" stroke="#1f6fb5"/></svg>tobias.wendt@dex9firm-example.at</li>
      <li><svg class="contact-icon" viewBox="0 0 12 12"><circle cx="6" cy="6" r="6" fill="#fff"/><circle cx="6" cy="6" r="3" fill="none" stroke="#1f6fb5"/></svg>dex9firm-example.at</li>
    </ul>

    <div class="holder-name">Tobias Wendt</div>
  </section>

  <section class="card card--back" aria-label="Business card back">
    <div class="wordmark">dex9firm</div>
    <div class="web-address">www.dex9firm-example.at</div>
  </section>

</main>
</body>
</html>
```